Larkspur Ridge Management - Business Cards

I need business cards. My current logo was designed by a designer at this site and I very much like and am happy with the results. I would like a business card that is trendy, unique, current yet professional. I deal with high net worth clients daily

Target Market(s)

Out of state investors looking to get into the rental market in Ohio

Industry/Entity Type

Property Management, Consulting

Contact Information for Business Card

Name, Title (Chief Financial Officer) office phone number (555) 817-3094 website address larkridgemgmt.example

Font styles to use
Sans Serif

Colors
0054AA
0677BA
7BADD7
CADEEF
E8F1F8
0094D4
00A9DD
6FCCEA
C7EBF8
E9F6FB
00AB8E
00BBA5
67D7C9
C6EFE9
E9F9F6

```html
<!DOCTYPE html>
<html lang="en">
<head>
<meta charset="utf-8">
<title>Larkspur Ridge Management – Business Cards</title>
<link href="https://fonts.googleapis.com/css2?family=Montserrat:wght@500;700&display=swap" rel="stylesheet">
<style>
  :root{
    --blue-deep:#0054AA;
    --blue-mid:#0677BA;
    --blue-soft:#7BADD7;
    --sky:#0094D4;
    --teal:#00AB8E;
    --teal-bright:#00BBA5;
    --paper:#E9F6FB;
    --backdrop:#ecebe8;
    --ink:#0b2f5c;
  }
  *{box-sizing:border-box;margin:0;padding:0}
  html,body{width:1200px;height:686px;overflow:hidden}
  body{
    position:relative;
    background:var(--backdrop);
    font-family:"Montserrat",Arial,sans-serif;
  }
  .card{
    position:absolute;
    left:255px;
    width:684px;
    border-radius:22px;
    overflow:hidden;
  }
  .card--front{top:20px;height:318px;background:var(--blue-deep)}
  .card--back{top:360px;height:300px;background:var(--paper)}

  .brand{
    position:absolute;
    display:flex;
    flex-direction:column;
    align-items:center;
    text-align:center;
  }
  .brand__mark{width:26px;height:26px;background:var(--teal);margin-bottom:14px}
  .brand__name{
    color:#fff;
    font-weight:700;
    text-transform:uppercase;
    line-height:1.15;
  }
  .card--front .brand{left:40px;top:74px;width:290px}
  .card--front .brand__name{font-size:30px;letter-spacing:1px}
  .divider{
    position:absolute;left:352px;top:56px;
    width:3px;height:218px;background:var(--teal);
  }
  .card__backdrop-art{
    position:absolute;left:380px;top:0;width:304px;height:318px;
    background:linear-gradient(200deg,rgba(123,173,215,.38) 0%,rgba(6,119,186,.22) 55%,rgba(0,84,170,0) 100%);
  }

  .card__angles{position:absolute;inset:0}
  .card--back .brand{left:425px;top:72px;width:220px}
  .card--back .brand__mark{width:20px;height:20px;margin-bottom:10px}
  .card--back .brand__name{font-size:22px;letter-spacing:.8px}

  .person{position:absolute;left:39px;top:60px}
  .person__name{
    font-size:27px;font-weight:700;color:var(--ink);letter-spacing:.3px;
  }
  .person__title{
    margin-top:4px;font-size:13.5px;font-weight:500;color:var(--teal);letter-spacing:.4px;
  }
  .rule{position:absolute;left:39px;width:68px;height:2px;background:var(--teal)}
  .rule--top{top:130px}
  .rule--bottom{top:243px}

  .contact{
    position:absolute;left:39px;
    display:flex;align-items:center;gap:14px;
    font-size:15.5px;font-weight:500;color:var(--ink);
  }
  .contact--phone{top:150px}
  .contact--web{top:192px}
  .contact__icon{
    width:35px;height:35px;display:flex;align-items:center;justify-content:center;
  }
  .contact--phone .contact__icon{background:var(--teal)}
  .contact--web .contact__icon{background:var(--blue-deep)}
</style>
</head>
<body>

<section class="card card--front" aria-label="Card front">
  <div class="brand">
    <span class="brand__mark"></span>
    <p class="brand__name">Larkspur<br>Ridge<br>Management</p>
  </div>
  <span class="divider"></span>
  <div class="card__backdrop-art" role="img" aria-label="Faint oversized brand decoration in soft blue tones"></div>
</section>

<section class="card card--back" aria-label="Card back">
  <svg class="card__angles" viewBox="0 0 684 300" width="684" height="300" aria-hidden="true">
    <polygon points="490,0 514,0 310,300 272,300 272,300" fill="var(--sky)"/>
    <polygon points="298,300 566,300 566,292 308,292" fill="var(--sky)"/>
    <polygon points="470,0 496,0 338,202 312,202" fill="var(--teal)"/>
    <polygon points="514,0 684,0 684,300 566,300 566,290 312,290" fill="var(--blue-deep)"/>
  </svg>

  <div class="person">
    <h1 class="person__name">YOUR NAME</h1>
    <p class="person__title">CHIEF FINANCIAL OFFICER</p>
  </div>
  <span class="rule rule--top"></span>

  <div class="contact contact--phone">
    <span class="contact__icon">
      <svg width="18" height="18" viewBox="0 0 24 24" aria-hidden="true">
        <path fill="#fff" d="M6.6 10.8a15.1 15.1 0 0 0 6.6 6.6l2.2-2.2a1 1 0 0 1 1-.25 11.4 11.4 0 0 0 3.6.57 1 1 0 0 1 1 1V20a1 1 0 0 1-1 1A17 17 0 0 1 3 4a1 1 0 0 1 1-1h3.5a1 1 0 0 1 1 1c0 1.25.2 2.45.57 3.57a1 1 0 0 1-.25 1z"/>
      </svg>
    </span>
    <span>(555) 817-3094</span>
  </div>

  <div class="contact contact--web">
    <span class="contact__icon">
      <svg width="19" height="19" viewBox="0 0 24 24" fill="none" stroke="#fff" stroke-width="1.6" aria-hidden="true">
        <circle cx="12" cy="12" r="9"/>
        <ellipse cx="12" cy="12" rx="4" ry="9"/>
        <line x1="3" y1="12" x2="21" y2="12"/>
        <line x1="4.5" y1="7.5" x2="19.5" y2="7.5"/>
        <line x1="4.5" y1="16.5" x2="19.5" y2="16.5"/>
      </svg>
    </span>
    <span>larkridgemgmt.example</span>
  </div>
  <span class="rule rule--bottom"></span>

  <div class="brand">
    <span class="brand__mark"></span>
    <p class="brand__name">Larkspur<br>Ridge<br>Management</p>
  </div>
</section>

</body>
</html>
```